DLM Homepage Banner

I would like a banner that uses/interprets the existing graphic on the www.janetholmcounsel.example homepage.

Target Market(s)

Business professionals across a variety of industries and sectors.

Requirements
Must have
• Must incorporate all the words and relationships of the existing image (file attached). I am seeking a professional and clean interpretation of the image.
• Must consider the look and feel of the banner on the following page: http://www.janetholmcounsel.example/pathways-in-nordic-crm/ (file attached)
• Must include the DLM logo in a similar style to the banner on the Pathways in Nordic CRM page (file attached).
Nice to have
• Feel free to add background/foreground graphics.
• I like the design idea of "bio-mechanical" applied to a professional services/business industry.
• The overall image must display a "business-technology-people-change" balance.
Should not have
• Should not be a direct replication of the existing graphic but must contain all the words and relationships.

```html
<!DOCTYPE html>
<html lang="en">
<head>
<meta charset="utf-8">
<title>DLM Homepage Banner</title>
<link rel="stylesheet" href="https://fonts.googleapis.com/css2?family=Nunito+Sans:wght@400;600;700;800;900&display=swap">
<style>
  :root{
    --navy:#0b5596;
    --navy-deep:#0a3f74;
    --sky:#0b8bcb;
    --sky-deep:#0a76b4;
    --tier:#1a8ac4;
    --tier-deep:#0f74ae;
    --grey-arrow:#6e6e6e;
    --label:#333338;
    --white:#ffffff;
    --logo:#123c7a;
    --muted:#5a5a5a;
    --link-line:#9fb7cf;
  }
  *{margin:0;padding:0;box-sizing:border-box}
  html,body{width:1200px;height:900px;overflow:hidden}
  body{font-family:"Nunito Sans",Arial,sans-serif}
  .banner{position:relative;width:1200px;height:900px;
    background:linear-gradient(180deg,#ffffff 0%,#ffffff 35%,#e9e9ea 70%,#bdbdbf 100%)}

  .risk-band{position:absolute;top:124px;height:86px;display:flex;flex-direction:column;
    justify-content:center;align-items:center;color:var(--white);text-align:center}
  .risk-band h2{font-weight:800;font-size:22px;letter-spacing:.2px;line-height:1.15}
  .risk-band p{font-weight:700;font-size:17px;margin-top:2px}
  .risk-procurement{left:63px;width:322px;background:var(--navy);padding-right:10px;
    clip-path:polygon(0 0,94.5% 0,100% 50%,94.5% 100%,0 100%)}
  .risk-independence{left:367px;width:460px;background:linear-gradient(180deg,var(--sky),var(--sky-deep));
    clip-path:polygon(0 0,95.5% 0,100% 50%,95.5% 100%,0 100%,4.5% 50%)}
  .risk-independence h2{font-size:30px;letter-spacing:.4px}
  .risk-independence p{font-weight:400;font-size:17.5px;letter-spacing:.3px;margin-top:0}
  .risk-business{left:802px;width:321px;background:var(--navy);padding-left:14px;
    clip-path:polygon(0 0,100% 0,100% 100%,0 100%,4.5% 50%)}

  .cycles{position:absolute;left:0;top:0}
  .cycle-label{font-family:"Nunito Sans",Arial,sans-serif;font-weight:900;font-size:18px;
    fill:var(--label);text-anchor:middle;dominant-baseline:middle;letter-spacing:.6px}
  .relation-line{fill:none;stroke:var(--link-line);stroke-width:1.5;stroke-dasharray:3 5}

  .framework-cap{position:absolute;left:437px;width:312px;height:32px;background:var(--sky-deep)}
  .cap-top{top:271px;clip-path:polygon(0 0,100% 0,87.5% 100%,12.5% 100%)}
  .cap-bottom{top:591px;clip-path:polygon(12.5% 0,87.5% 0,100% 100%,0 100%)}
  .framework-tier{position:absolute;left:476px;width:239px;height:50px;
    background:linear-gradient(180deg,var(--tier),var(--tier-deep));color:var(--white);
    display:flex;align-items:center;justify-content:center;font-weight:800;font-size:19px}

  .role-arrow{position:absolute;left:473px;width:262px;height:39px;background:var(--grey-arrow);
    clip-path:polygon(0 0,93% 0,100% 50%,93% 100%,0 100%);color:#ececec;
    display:flex;align-items:center;justify-content:center;font-weight:800;font-size:16.5px;padding-right:14px}

  .brand{position:absolute;left:86px;top:712px;font-family:"Nunito Sans",Arial,sans-serif;
    font-weight:800;font-size:24px;color:var(--logo);display:flex;align-items:center;gap:10px}
  .brand-mark{width:16px;height:16px;background:var(--logo)}
  .source-note{position:absolute;left:912px;top:742px;font-family:"Nunito Sans",Arial,sans-serif;
    font-weight:400;font-size:15px;color:var(--muted)}
</style>
</head>
<body>
<main class="banner">
  <div class="risk-band risk-procurement"><h2>PROCUREMENT RISK</h2><p>The right Partner</p></div>
  <div class="risk-band risk-independence"><h2>INDEPENDENCE RISK</h2><p>THE RIGHT TECHNOLOGY FRAMEWORK</p></div>
  <div class="risk-band risk-business"><h2>BUSINESS RISK</h2><p>The right Outcome</p></div>

  <svg class="cycles" width="1200" height="900" viewBox="0 0 1200 900">
    <defs>
      <radialGradient id="ring-shade" gradientUnits="userSpaceOnUse" cx="0" cy="0" r="215">
        <stop offset="0.83" stop-color="#0c4a88"/>
        <stop offset="0.9" stop-color="#1e6db3"/>
        <stop offset="0.97" stop-color="#0d4f8f"/>
        <stop offset="1" stop-color="#093e72"/>
      </radialGradient>
      <path id="cycle-step" fill="url(#ring-shade)"
        d="M3.75,-214.97 A215,215 0 0 1 200.72,-77.05 L188.39,-57.6 L167.11,-64.15 A179,179 0 0 0 3.12,-178.97 L17.17,-196.25 Z"/>
    </defs>

    <path class="relation-line" d="M445 447 H476"/>
    <path class="relation-line" d="M715 447 H745"/>

    <g class="cycle-procurement" transform="translate(230 447)">
      <use href="#cycle-step"/>
      <use href="#cycle-step" transform="rotate(72)"/>
      <use href="#cycle-step" transform="rotate(144)"/>
      <use href="#cycle-step" transform="rotate(216)"/>
      <use href="#cycle-step" transform="rotate(288)"/>
    </g>
    <g class="cycle-procurement-labels">
      <text class="cycle-label" transform="translate(146 328) rotate(-35)">UPGRADE</text>
      <text class="cycle-label" transform="translate(314 330) rotate(35)">EVALUATE</text>
      <text class="cycle-label" transform="translate(362 490) rotate(-72)">PROCURE</text>
      <text class="cycle-label" transform="translate(228 586) rotate(4)">IMPLEMENT</text>
      <text class="cycle-label" transform="translate(95 482) rotate(72)">MAINTAIN</text>
    </g>

    <g class="cycle-business" transform="translate(960 447)">
      <use href="#cycle-step"/>
      <use href="#cycle-step" transform="rotate(72)"/>
      <use href="#cycle-step" transform="rotate(144)"/>
      <use href="#cycle-step" transform="rotate(216)"/>
      <use href="#cycle-step" transform="rotate(288)"/>
    </g>
    <g class="cycle-business-labels">
      <text class="cycle-label" transform="translate(878 330) rotate(-35)">GOVERN</text>
      <text class="cycle-label" transform="translate(1046 334) rotate(38)">CHANGE</text>
      <text class="cycle-label" transform="translate(1085 488) rotate(-70)">COMMUNICATE</text>
      <text class="cycle-label" transform="translate(960 590) rotate(4)">PROCESS</text>
      <text class="cycle-label" transform="translate(830 480) rotate(74)">IMPLEMENT</text>
    </g>
  </svg>

  <div class="framework-cap cap-top"></div>
  <div class="framework-tier" style="top:310px">Enterprise Strategy</div>
  <div class="framework-tier" style="top:366px">Enterprise Software</div>
  <div class="framework-tier" style="top:422px">Enterprise Hardware</div>
  <div class="framework-tier" style="top:478px">Enterprise Networks</div>
  <div class="framework-tier" style="top:534px">Enterprise Services</div>
  <div class="framework-cap cap-bottom"></div>

  <div class="role-arrow" style="top:631px">Analysts</div>
  <div class="role-arrow" style="top:677px">Advisors</div>
  <div class="role-arrow" style="top:724px">Programme Managers</div>

  <div class="brand"><span class="brand-mark"></span>DLM Janet Holm Counsel</div>
  <p class="source-note">Source: Janet Holm Counsel 2013</p>
</main>
</body>
</html>
```